Pipelining Product Supply Company Needs New Stationery

We need new stationery (letter head, with compliments slips & business card) for our industry leading pipe lining supply company. basically we sell product to other plumbers to carry out pipe relining.

Im looking for something, fresh, professional, sleek and modern at the same time.

Ive attached a copy of the logo and also some guidelines to follow for colours and fonts etc.

Target Market(s)

Plumbers

Industry/Entity Type

Plumbing

Font styles to use
Sans Serif

Requirements
Must have
• The logo, space for ABN, Address, Phone Number, website and email.
Nice to have
• Stand out from the crowd. To look sleep and professional.
Should not have
• Any other colours apart from what is on the guidelines.

```html
<!DOCTYPE html>
<html lang="en">
<head>
<meta charset="utf-8">
<title>Northline Relining Supplies – Stationery</title>
<link href="https://fonts.googleapis.com/css2?family=Questrial&display=swap" rel="stylesheet">
<style>
  :root{
    --green:#8dc63f;
    --black:#0e0e0e;
    --grey:#9a9a9a;
    --paper:#ffffff;
    --stage-top:#e4e8e7;
    --stage-bottom:#e9e9e9;
    --divider:#9b9b9b;
    --ink:#333333;
  }
  *{box-sizing:border-box;margin:0;padding:0}
  html,body{width:1200px;height:1200px;overflow:hidden}
  body{font-family:"Questrial",sans-serif;position:relative;background:var(--stage-bottom)}
  .stage-top{position:absolute;left:0;top:0;width:1200px;height:590px;background:var(--stage-top)}
  .divider{position:absolute;left:0;top:590px;width:1200px;height:16px;background:var(--divider)}
  .stage-bottom{position:absolute;left:0;top:606px;width:1200px;height:594px;background:var(--stage-bottom)}

  .brand{color:var(--green);letter-spacing:.04em;text-transform:uppercase;line-height:1.15}

  /* Compliments slip */
  .comp-slip{position:absolute;left:110px;top:110px;width:470px;height:222px;background:var(--black);box-shadow:0 6px 18px rgba(0,0,0,.18)}
  .comp-slip .holder{position:absolute;left:22px;top:18px}
  .comp-slip .holder-name{color:var(--green);font-size:11px}
  .comp-slip .holder-role,.comp-slip .holder-contact{color:#fff;font-size:7px;margin-top:3px}
  .comp-slip .brand{position:absolute;right:24px;top:82px;font-size:17px;text-align:right;width:200px}
  .comp-slip .greeting{position:absolute;right:24px;bottom:18px;color:var(--green);font-size:14px}

  /* Letterhead */
  .letterhead{position:absolute;left:650px;top:40px;width:370px;height:523px;background:var(--paper);box-shadow:0 6px 18px rgba(0,0,0,.18);overflow:hidden;color:var(--ink)}
  .letterhead .contact{position:absolute;left:24px;top:16px;font-size:6.5px;line-height:1.6}
  .letterhead .contact li{list-style:none;display:flex;align-items:center;gap:4px}
  .icon-dot{display:inline-block;width:6px;height:6px;border-radius:50%;background:var(--black)}
  .letterhead .brand-block{position:absolute;right:22px;top:18px;width:58px;height:58px;background:var(--black);display:flex;align-items:center;justify-content:center;text-align:center}
  .letterhead .brand-block .brand{font-size:7px}
  .letterhead .recipient{position:absolute;left:24px;top:90px;font-size:7px;line-height:1.5}
  .letterhead .recipient p+p{margin-top:6px}
  .letterhead .body{position:absolute;left:24px;top:175px;width:320px;font-size:7px;line-height:1.7;color:#555}
  .letterhead .body p{margin-bottom:8px}
  .letterhead .sign-off{position:absolute;right:30px;top:385px;font-size:7px;text-align:left}
  .letterhead .sign-off .signer{margin-top:8px;font-size:7px;color:#555}
  .letterhead .footer-band{position:absolute;left:0;bottom:0;width:370px;height:80px}

  /* Business cards */
  .card{position:absolute;width:430px;height:246px;background:var(--black);box-shadow:0 10px 24px rgba(0,0,0,.22);overflow:hidden}
  .card-back{left:120px;top:780px}
  .card-front{left:650px;top:700px}
  .card .strip{position:absolute;left:0;bottom:0;width:430px;height:60px}
  .card-back .brand{position:absolute;left:0;top:78px;width:430px;text-align:center;font-size:26px}
  .card-back .web{position:absolute;right:30px;bottom:12px;color:var(--black);font-size:9px;letter-spacing:.18em}
  .card-front .holder{position:absolute;left:26px;top:42px}
  .card-front .holder-name{color:var(--green);font-size:18px}
  .card-front .holder-role{color:#fff;font-size:11px;margin-top:3px}
  .card-front .brand{position:absolute;right:26px;top:38px;font-size:17px;text-align:right;width:200px}
  .card-front .contact{position:absolute;right:26px;top:112px;list-style:none;text-align:right;font-size:9.5px;line-height:1.65;color:var(--green)}
  .card-front .contact li{display:flex;align-items:center;justify-content:flex-end;gap:6px}
  .card-front .contact .icon-dot{background:#cfcfcf;width:7px;height:7px}
  .card-front .abn{position:absolute;right:30px;bottom:12px;color:var(--black);font-size:9px;letter-spacing:.2em}
</style>
</head>
<body>
  <div class="stage-top"></div>
  <div class="divider"></div>
  <div class="stage-bottom"></div>

  <section class="comp-slip" aria-label="With compliments slip">
    <div class="holder">
      <p class="holder-name">Dana Mercer</p>
      <p class="holder-role">Training Specialist</p>
      <p class="holder-contact">1-300-555-014 | 12 Harlow Street Westmead NSW 2145</p>
      <p class="holder-contact">northlinerelining.com.au | hello@northlinerelining.com.au</p>
    </div>
    <p class="brand">Northline Relining Supplies</p>
    <p class="greeting">with compliments</p>
  </section>

  <section class="letterhead" aria-label="Letterhead">
    <ul class="contact">
      <li><span class="icon-dot"></span>1-300-555-014</li>
      <li><span class="icon-dot"></span>12 Harlow Street Westmead NSW 2145</li>
      <li><span class="icon-dot"></span>hello@northlinerelining.com.au</li>
    </ul>
    <div class="brand-block"><p class="brand">Northline Relining Supplies</p></div>
    <div class="recipient">
      <p>Date</p>
      <p>Recipient Name</p>
      <p>Company Name<br>Street Address<br>City, State, Zip</p>
    </div>
    <div class="body">
      <p>Thank you for your recent enquiry about our relining range. We are pleased to confirm that the requested liners, resins and inversion gear are now in stock and ready for dispatch to your depot this week.</p>
      <p>Our training team can also visit your site to take your crew through setup, curing times and safe handling of each product.</p>
      <p>Please call us on the number above if you have any questions about pricing, delivery or stock levels.</p>
      <p>We look forward to working with you again.</p>
    </div>
    <div class="sign-off">
      <p>Sincerely Yours,</p>
      <p class="signer">Dana Mercer</p>
    </div>
    <svg class="footer-band" viewBox="0 0 370 80" aria-hidden="true">
      <rect x="0" y="34" width="370" height="3" fill="var(--green)"/>
      <polygon points="0,40 130,40 140,52 370,52 370,80 0,80" fill="var(--black)"/>
    </svg>
  </section>

  <section class="card card-back" aria-label="Business card, brand side">
    <p class="brand">Northline<br>Relining Supplies</p>
    <svg class="strip" viewBox="0 0 430 60" aria-hidden="true">
      <polygon points="0,8 150,8 160,16 430,16 430,22 0,22" fill="var(--grey)"/>
      <polygon points="0,22 430,22 430,38 0,38" fill="var(--green)"/>
      <polygon points="0,38 110,38 120,30 430,30 430,60 0,60" fill="var(--green)"/>
    </svg>
    <p class="web">northlinerelining.com.au</p>
  </section>

  <section class="card card-front" aria-label="Business card, contact side">
    <div class="holder">
      <p class="holder-name">Dana Mercer</p>
      <p class="holder-role">Training Specialist</p>
    </div>
    <p class="brand">Northline<br>Relining Supplies</p>
    <ul class="contact">
      <li>1-300-555-014<span class="icon-dot"></span></li>
      <li>12 Harlow Street Westmead NSW 2145<span class="icon-dot"></span></li>
      <li>northlinerelining.com.au<span class="icon-dot"></span></li>
      <li>hello@northlinerelining.com.au<span class="icon-dot"></span></li>
    </ul>
    <svg class="strip" viewBox="0 0 430 60" aria-hidden="true">
      <polygon points="0,14 430,14 430,20 0,20" fill="var(--grey)"/>
      <polygon points="0,20 430,20 430,34 0,34" fill="var(--green)"/>
      <polygon points="0,34 110,34 120,30 430,30 430,60 0,60" fill="var(--green)"/>
    </svg>
    <p class="abn">ABN 12 345 678 901</p>
  </section>
</body>
</html>
```